bean bag mailer

We manufacture bean bag chairs in Dallas. We want to send out a mailer to all of the daycares and churches in Dallas and surrounding areas. Summer time is very busy for these daycares, and we would like to offer fun, functional, and affordable furniture for them to use. We want the postcard to be very bright and attractive to kids.

Target Market(s)

We're targeting daycares and churches

Industry/Entity Type

Manufacture

Requirements
Must have
• We want the logo. We also want the phone number, which is 214-637-4182. We offer bulk discounts such as 5% off orders of at least 15. 10% off orders of at least 25. 20% off orders of at least 50. We would also like to note that these bags are made in the U.S.A.
Nice to have
• Want the postcard to be really bright, colorful, and eye-catching. The pics of the bean bags are just examples, other images can be used if they better fit the layout.

```html
<!DOCTYPE html>
<html lang="en">
<head>
<meta charset="utf-8">
<title>Trinity Bean Bags – Mailer</title>
<link rel="stylesheet" href="https://fonts.googleapis.com/css2?family=Oswald:wght@500;700&family=Open+Sans:wght@400;700;800&display=swap">
<style>
  :root{
    --stage:#000;
    --card:#fff;
    --ink:#111;
    --red:#e0262f;
    --ribbon-top:#3fb3e6;
    --ribbon-bottom:#0b63a8;
    --accent-yellow:#f6e62a;
    --grey:#8a8a8a;
    --line:#9a9a9a;
    --row-yellow:#f8ee8e;
    --row-green:#7dc57f;
    --row-pink:#eec6dd;
    --row-blue:#88d4e8;
    --row-orange:#f9c98a;
    --phone-ring:#5bbf4a;
  }
  *{box-sizing:border-box;margin:0;padding:0}
  html,body{width:1200px;height:950px;overflow:hidden;background:var(--stage)}
  .stage{position:relative;width:1200px;height:950px;font-family:"Open Sans",Arial,sans-serif}
  .card{position:absolute;background:var(--card)}
  .card--front{left:304px;top:13px;width:588px;height:456px}
  .card--back{left:304px;top:478px;width:589px;height:457px}

  /* brand name */
  .brand{position:absolute;display:flex;align-items:center;gap:10px;
    font-family:"Oswald",sans-serif;font-weight:700;color:var(--ink);letter-spacing:1px;white-space:nowrap}
  .brand__dot{display:block;border-radius:50%;background:var(--accent-yellow)}
  .card--front .brand{left:48px;top:36px;font-size:44px;line-height:1}
  .card--front .brand__dot{width:34px;height:34px}

  /* front */
  .hero-photo{position:absolute;left:31px;top:100px;width:362px;height:270px;
    background:linear-gradient(160deg,#8a4bb0 0%,#6a3592 55%,#55287a 100%)}
  .discount{position:absolute;right:0;height:71px;color:#fff;
    background:linear-gradient(180deg,var(--ribbon-top),var(--ribbon-bottom));
    clip-path:polygon(3% 0,100% 0,100% 100%,0 100%)}
  .discount--5{top:100px;width:202px}
  .discount--10{top:180px;width:194px}
  .discount--20{top:260px;width:186px}
  .discount__value{position:absolute;left:24px;top:4px;font-family:"Oswald",sans-serif;font-weight:700;font-size:42px;line-height:1;color:var(--accent-yellow)}
  .discount__value small{font-size:28px;color:#fff;margin-left:4px}
  .discount__terms{position:absolute;left:26px;bottom:8px;font-size:10.5px;font-weight:800;letter-spacing:.2px}
  .discount__terms b{color:var(--accent-yellow)}
  .made-in{position:absolute;left:42px;top:396px;display:flex;align-items:center;gap:6px}
  .made-in__small{font-family:"Oswald",sans-serif;font-weight:700;font-size:13px;line-height:.95;color:var(--ink)}
  .made-in__big{font-family:"Oswald",sans-serif;font-weight:700;font-size:32px;line-height:1;color:var(--ink)}
  .flag{margin-left:6px}
  .call-front{position:absolute;left:243px;top:370px;display:flex;align-items:center;gap:2px}
  .call-front__label{font-family:"Oswald",sans-serif;font-weight:700;font-size:18px;line-height:1.1;color:var(--ink)}
  .phone-number{font-family:"Oswald",sans-serif;font-weight:700;color:var(--red);white-space:nowrap}
  .card--front .phone-number{position:absolute;left:375px;top:386px;font-size:33px}

  /* back */
  .banner{position:absolute;left:0;top:0;width:443px;height:117px;overflow:hidden;
    background:linear-gradient(170deg,#f3e222 0%,#8cc63f 40%,#6cbd45 65%,#e6f3d3 100%)}
  .card--back .brand{left:14px;top:72px;font-size:26px;line-height:1}
  .card--back .brand__dot{width:20px;height:20px}
  .banner__bags{position:absolute;left:326px;top:70px;width:116px;height:42px;
    background:linear-gradient(90deg,#2a47a8,#3a3a44 50%,#c8343f)}
  .stamp{position:absolute;left:477px;top:51px;width:67px;height:76px;border:1.5px solid #b5b5b5;
    color:var(--grey);font-family:Arial,sans-serif;font-size:12.5px;line-height:15px;text-align:center;padding-top:17px}
  .features{position:absolute;left:0;top:118px;width:285px;list-style:none}
  .features li{height:16.6px;padding-left:53px;font-family:Arial,sans-serif;font-size:13.5px;line-height:16.6px;color:var(--ink);position:relative}
  .features li::before{content:"";position:absolute;left:41px;top:3px;width:4px;height:8px;border:solid var(--red);border-width:0 2px 2px 0;transform:rotate(40deg)}
  .features li:nth-child(1){background:var(--row-yellow)}
  .features li:nth-child(2){background:var(--row-green)}
  .features li:nth-child(3){background:var(--row-pink)}
  .features li:nth-child(4){background:var(--row-blue)}
  .features li:nth-child(5){background:var(--row-orange)}
  .features li:nth-child(6){background:var(--row-yellow)}
  .bag-stack{position:absolute;left:82px;top:225px;width:126px;height:94px;
    background:linear-gradient(180deg,#c7a6d4 0%,#e39aa6 55%,#c8434d 100%)}
  .call-back{position:absolute;left:39px;top:320px;display:flex;align-items:center;gap:20px}
  .call-back__label{font-family:"Oswald",sans-serif;font-weight:700;font-size:17px;line-height:1;color:var(--red)}
  .card--back .phone-number{font-size:23px;color:#333;line-height:1.1}
  .address-line{position:absolute;left:310px;width:210px;border-top:1.5px solid var(--line)}
</style>
</head>
<body>
<div class="stage">

  <section class="card card--front">
    <div class="brand"><span class="brand__dot"></span>TRINITY Bean Bags</div>
    <div class="hero-photo" role="img" aria-label="Photo of colourful bean bag chairs with two children seated on a large purple bean bag"></div>

    <div class="discount discount--5"><div class="discount__value">5%<small>OFF</small></div><div class="discount__terms">ON ORDERS ATLEAST <b>15</b></div></div>
    <div class="discount discount--10"><div class="discount__value">10%<small>OFF</small></div><div class="discount__terms">ON ORDERS ATLEAST <b>25</b></div></div>
    <div class="discount discount--20"><div class="discount__value">20%<small>OFF</small></div><div class="discount__terms">ON ORDERS ATLEAST <b>50</b></div></div>

    <div class="made-in">
      <div class="made-in__small">MADE<br>IN THE</div>
      <div class="made-in__big">USA</div>
      <svg class="flag" width="50" height="27" viewBox="0 0 50 27" aria-hidden="true">
        <rect width="50" height="27" fill="#fff"/>
        <g fill="#d42a2a"><rect y="0" width="50" height="2.1"/><rect y="4.2" width="50" height="2.1"/><rect y="8.4" width="50" height="2.1"/><rect y="12.6" width="50" height="2.1"/><rect y="16.8" width="50" height="2.1"/><rect y="21" width="50" height="2.1"/><rect y="25" width="50" height="2"/></g>
        <rect width="21" height="14.6" fill="#2a3f8f"/>
      </svg>
    </div>

    <div class="call-front">
      <svg width="58" height="62" viewBox="0 0 58 62" aria-hidden="true">
        <path d="M44 8 A27 27 0 1 0 44 54" fill="none" stroke="var(--phone-ring)" stroke-width="3"/>
        <path d="M22 12 q-8 2 -8 19 q0 17 8 19 l6 -1 q2 -1 1 -4 l-3 -8 q-1 -2 -4 -1 q-2 -6 0 -12 q3 1 4 -1 l3 -8 q1 -3 -1 -4z" fill="var(--red)"/>
      </svg>
      <div class="call-front__label">CALL US<br>TODAY!</div>
    </div>
    <div class="phone-number">214-637-4182</div>
  </section>

  <section class="card card--back">
    <div class="banner">
      <div class="brand"><span class="brand__dot"></span>TRINITY Bean Bags</div>
      <div class="banner__bags" role="img" aria-label="Photo of blue, black and red bean bags"></div>
    </div>
    <div class="stamp">Place<br>Stamp<br>Here</div>

    <ul class="features">
      <li>Alternative Furniture</li>
      <li>Great Selection</li>
      <li>Vivid Colors</li>
      <li>Featuring High Quality Materials</li>
      <li>Comfortable</li>
      <li>Affordable Bean Bags</li>
    </ul>

    <div class="bag-stack" role="img" aria-label="Photo of small coloured bean bags stacked together"></div>

    <div class="call-back">
      <svg width="52" height="50" viewBox="0 0 52 50" aria-hidden="true">
        <path d="M26 3 C12 3 3 12 3 23 c0 8 5 14 12 17 l-3 8 l11 -6 c1 0 2 0 3 0 c14 0 23 -9 23 -19 S40 3 26 3z" fill="#fff" stroke="#555" stroke-width="2.5"/>
        <path d="M20 12 q-6 2 -5 11 q1 9 8 13 l4 -1 q2 -1 1 -3 l-2 -5 q-1 -2 -3 -1 q-3 -4 -2 -8 q2 0 3 -1 l1 -5 q0 -2 -2 -2z" fill="#e8552a"/>
      </svg>
      <div>
        <div class="call-back__label">CALL NOW!</div>
        <div class="phone-number">214-637-4182</div>
      </div>
    </div>

    <div class="address-line" style="top:243px"></div>
    <div class="address-line" style="top:285px"></div>
    <div class="address-line" style="top:328px"></div>
  </section>

</div>
</body>
</html>
```